Single Webpage Custom Design

We need a single page for a service-offering on http://insight.brovantide.com/. I created a draft so you can see what content should be on that page.

```html
<!DOCTYPE html>
<html lang="en">
<head>
<meta charset="utf-8">
<title>Brovantide – Security Awareness E-Learning</title>
<link href="https://fonts.googleapis.com/css2?family=Poppins:wght@300;400;500;600;700&display=swap" rel="stylesheet">
<style>
:root{
  --teal:#1aa6ad;
  --teal-dark:#11858b;
  --orange:#f6a21e;
  --orange-dark:#d9830a;
  --grey-badge:#7d8084;
  --grey-badge-dark:#5e6165;
  --ink:#2f3236;
  --body:#55595e;
  --soft:#f2f4f7;
  --line:#e3e6ea;
  --white:#ffffff;
}
*{margin:0;padding:0;box-sizing:border-box}
html,body{width:1200px;height:4103px;overflow:hidden}
body{position:relative;font-family:"Poppins",sans-serif;color:var(--body);background:var(--white)}
.abs{position:absolute}
.center{text-align:center}
.hero{left:0;top:0;width:1200px;height:512px;background:linear-gradient(135deg,#22b3b9 0%,#17a0a7 60%,#1596a0 100%)}
.brand{left:88px;top:48px;display:flex;align-items:center;gap:10px;font-weight:700;font-size:30px;color:#ffd23a}
.brand-dot{width:26px;height:26px;border-radius:50%;background:#ffd23a}
.hero-title{left:0;width:1200px;top:172px;font-weight:700;font-size:36px;line-height:40px;color:var(--white);letter-spacing:.5px}
.hero-visual{left:330px;top:285px;width:545px;height:300px;border-radius:14px;background:linear-gradient(180deg,#1f6f74,#0f4f55);box-shadow:0 18px 30px rgba(0,0,0,.12)}
.hero-visual::after{content:"";position:absolute;left:30px;top:26px;right:30px;bottom:18px;background:#f4f7f8;border-radius:4px}
h2.lead{left:0;width:1200px;top:652px;font-weight:600;font-size:34px;color:var(--ink)}
.lead-sub{left:0;width:1200px;top:700px;font-size:18px;font-weight:300}
.divider{left:88px;top:786px;width:1023px;height:1px;background:var(--line)}
.section-title{left:0;width:1200px;font-weight:600;font-size:32px;color:var(--ink)}
.teal-title{color:var(--teal);font-weight:700}
.badge{width:136px;height:108px}
.step1-title{left:150px;width:350px;top:1088px;font-size:35px;line-height:42px}
.design-info{left:601px;top:970px;width:520px}
.design-info h3{font-weight:500;font-size:24px;line-height:30px;color:var(--ink)}
.design-info p{font-size:14.5px;line-height:21px;margin-top:10px;font-weight:300;color:var(--ink)}
.design-info ul{list-style:none;margin-top:10px}
.design-info li{font-size:14.5px;line-height:21.5px;font-weight:300;color:var(--ink);padding-left:16px;position:relative}
.design-info li::before{content:"";position:absolute;left:0;top:7px;width:8px;height:8px;border-radius:50%;background:var(--orange)}
.explore{left:0;width:1200px;top:1258px;font-size:27px}
.type{width:340px;text-align:center}
.type .icon{width:96px;height:96px;border-radius:50%;margin:0 auto}
.type h4{margin-top:22px;font-weight:500;font-size:20px;color:var(--ink)}
.type p{margin-top:6px;font-size:14.5px;line-height:21px;font-weight:300;color:var(--ink)}
.band-soft{left:0;width:1200px;background:var(--soft)}
.topics-title{top:1785px;font-size:35px}
.topics-sub{left:0;width:1200px;top:1852px;font-weight:500;font-size:22px;color:var(--ink)}
.topics-text{left:190px;width:820px;top:1887px;font-size:14.5px;line-height:22px;font-weight:300;color:var(--ink)}
.card{top:1964px;width:327px;height:290px;background:var(--white);border-radius:6px;box-shadow:0 6px 24px rgba(0,0,0,.07);text-align:center}
.card .pic{width:130px;height:120px;margin:56px auto 0;border-radius:8px;background:#dff2f3}
.card h5{margin-top:30px;font-weight:500;font-size:21px;color:var(--ink)}
.card.active{background:var(--teal)}
.card.active .pic{background:rgba(255,255,255,.2)}
.card.active h5{color:var(--white)}
.customize-title{top:2524px;font-size:35px}
.customize-text{left:220px;width:760px;top:2572px;font-size:14.5px;line-height:22px;font-weight:300;color:var(--ink)}
.example{width:520px;text-align:center}
.example h4{font-weight:500;font-size:21px;color:var(--ink)}
.example p{margin-top:4px;font-size:14.5px;line-height:22px;font-weight:300;color:var(--ink)}
.message-title{left:84px;top:3048px;font-size:35px}
.message-text{left:84px;top:3105px;width:510px;font-size:14.5px;line-height:21.5px;font-weight:300;color:var(--ink)}
.export-title{left:638px;top:3430px;font-weight:600;font-size:35px;color:var(--ink)}
.export-text{left:638px;top:3482px;width:470px;font-size:14.5px;line-height:21.5px;font-weight:300;color:var(--body)}
.footer{left:0;top:3631px;width:1200px;height:472px;background:var(--teal);color:var(--white)}
.f-head{font-weight:500;font-size:19px;letter-spacing:.3px;color:var(--white)}
.f-lines{font-size:17px;line-height:26.5px;font-weight:300;color:#f1fbfb}
.search{left:465px;top:3799px;width:232px;height:40px;border:1px solid #e9f6f7;background:var(--white);display:flex}
.search span{flex:1;font-size:15px;color:#333;padding:9px 10px}
.search i{width:40px;border-left:1px solid #d6e3e4;display:flex;align-items:center;justify-content:center}
.social{left:465px;top:3932px;display:flex;align-items:center;gap:12px;font-size:15px}
.social .dot{width:36px;height:36px;border-radius:50%;background:#3a5a98}
.lang{left:995px;top:3792px;font-size:15px;display:flex;align-items:center;gap:18px}
.f-rule{left:88px;top:4050px;width:1023px;height:1px;background:rgba(255,255,255,.55)}
.copyright{left:0;width:1200px;top:4068px;font-size:14px;color:var(--white)}
.to-top{left:1119px;top:4036px;width:32px;height:32px;border-radius:50%;background:var(--orange);display:flex;align-items:center;justify-content:center}
</style>
</head>
<body>

<header class="abs hero">
  <div class="abs brand"><span class="brand-dot"></span>Brovantide</div>
  <h1 class="abs hero-title center">Security&nbsp; Awarness E-Learning<br>You Can Run In Your Environment</h1>
</header>
<div class="abs hero-visual" role="img" aria-label="Laptop screen showing a security awareness training course at 60% progress, with mascot characters on both sides"></div>

<h2 class="abs lead center">Choose one or multiple training modules</h2>
<p class="abs lead-sub center">from Brovantide Security and import them into your Learning management system (LMS) via SCORM.</p>
<div class="abs divider"></div>

<h2 class="abs section-title center" style="top:872px">How Does It Work?</h2>

<svg class="abs badge" style="left:260px;top:971px" viewBox="0 0 136 108" aria-hidden="true">
  <polygon points="0,18 18,0 118,0 136,18" fill="var(--grey-badge-dark)"/>
  <rect x="10" y="10" width="116" height="98" rx="10" fill="var(--grey-badge)"/>
  <text x="68" y="50" text-anchor="middle" font-family="Poppins,sans-serif" font-size="24" font-weight="300" fill="#fff">STEP</text>
  <text x="68" y="88" text-anchor="middle" font-family="Poppins,sans-serif" font-size="32" font-weight="700" fill="#fff">№1</text>
</svg>
<h3 class="abs step1-title teal-title center">Choose Your<br>Prefered Design</h3>

<div class="abs design-info">
  <h3>Design is more than just Layout - It is about the desired user experience</h3>
  <p>The same topic can be presented in different designs and formats.<br>There is no right or wrong - it is all about your goals.</p>
  <ul>
    <li>Do you want to include videos in the course?</li>
    <li>Should the text be read to the user?</li>
    <li>Do you want to include a game or exam at the end of the course?</li>
    <li>Do you want to guide the user with an avatar through the course? etc.</li>
  </ul>
</div>

<h3 class="abs explore teal-title center">Explore a few design types</h3>

<div class="abs type" style="left:88px;top:1342px">
  <div class="icon" role="img" aria-label="Avatar design icon" style="background:linear-gradient(180deg,#8fc3ea,#3d8ad0)"></div>
  <h4>Avatar Design</h4>
  <p>Lorem Ipsum is simply dummy text<br>of the printing and typesetting industry.<br>Lorem Ipsum has been.</p>
</div>
<div class="abs type" style="left:429px;top:1342px">
  <div class="icon" role="img" aria-label="Classic design icon" style="background:linear-gradient(180deg,#5aa6e0,#2b6fb0)"></div>
  <h4>Classic Design</h4>
  <p>Lorem Ipsum is simply dummy text<br>of the printing and typesetting industry.<br>Lorem Ipsum has been.</p>
</div>
<div class="abs type" style="left:769px;top:1342px">
  <div class="icon" role="img" aria-label="One pager design icon" style="background:linear-gradient(180deg,#f7b63b,#3f7fc4)"></div>
  <h4>One Pager</h4>
  <p>Lorem Ipsum is simply dummy text<br>of the printing and typesetting industry.<br>Lorem Ipsum has been.</p>
</div>

<div class="abs band-soft" style="top:1651px;height:718px"></div>

<svg class="abs badge" style="left:532px;top:1635px" viewBox="0 0 136 108" aria-hidden="true">
  <polygon points="0,18 18,0 118,0 136,18" fill="var(--orange-dark)"/>
  <rect x="10" y="10" width="116" height="98" rx="10" fill="var(--orange)"/>
  <text x="68" y="50" text-anchor="middle" font-family="Poppins,sans-serif" font-size="24" font-weight="300" fill="#fff">STEP</text>
  <text x="68" y="88" text-anchor="middle" font-family="Poppins,sans-serif" font-size="32" font-weight="700" fill="#fff">№2</text>
</svg>

<h2 class="abs section-title topics-title teal-title center">Choose Your Topics</h2>
<p class="abs topics-sub center">Select The Topics and The Specfiy The course Length</p>
<p class="abs topics-text center">Brovantide comes with +250 out of the box awarness trainings for end users.All courses can be customized-or we can create your individual courses from scratch.Use the standard tralings or create a custom version.</p>

<div class="abs card" style="left:86px">
  <div class="pic" role="img" aria-label="Line illustration of a person at a desk with a chat bubble"></div>
  <h5>Standard Training</h5>
</div>
<div class="abs card active" style="left:437px">
  <div class="pic" role="img" aria-label="Line illustration of a person in front of charts and settings"></div>
  <h5>Customized Taining</h5>
</div>
<div class="abs card" style="left:783px">
  <div class="pic" role="img" aria-label="Line illustration of a person presenting at a board"></div>
  <h5>Individual Training</h5>
</div>

<svg class="abs" style="left:526px;top:2353px" width="136" height="108" viewBox="0 0 136 108" aria-hidden="true">
  <polygon points="0,18 18,0 118,0 136,18" fill="var(--teal-dark)"/>
  <rect x="10" y="10" width="116" height="98" rx="10" fill="var(--teal)"/>
  <text x="68" y="50" text-anchor="middle" font-family="Poppins,sans-serif" font-size="24" font-weight="300" fill="#fff">STEP</text>
  <text x="68" y="88" text-anchor="middle" font-family="Poppins,sans-serif" font-size="32" font-weight="700" fill="#fff">№3</text>
</svg>

<h2 class="abs section-title customize-title teal-title center">Customize!</h2>
<p class="abs customize-text center">You might ask yourself why it needs customization? Beside just adjusting the design (logo, font, colours) to your corporate look and feel, it is important that the users perceives the training as something they can really relate to. Examples:</p>

<div class="abs" style="left:210px;top:2705px;width:230px;height:148px;background:linear-gradient(135deg,#c9c3bb,#3c4a55 60%,#1aa6ad)" role="img" aria-label="Photos of a video call with a company executive, with teal and orange accent squares"></div>
<div class="abs" style="left:743px;top:2699px;width:223px;height:170px;background:linear-gradient(135deg,#1aa6ad 0%,#eef1f3 35%,#eef1f3 75%,#f6a21e 100%)" role="img" aria-label="Screenshot of a company policy document with teal and orange accents"></div>

<div class="abs example" style="left:84px;top:2876px">
  <h4>From CEO</h4>
  <p>Add a personal greeting note from your CEO at the start of<br>the training to highlight the importance of the training</p>
</div>
<div class="abs example" style="left:596px;top:2876px">
  <h4>Do you know our policies?</h4>
  <p>You could ask your user to read and acknowledge your<br>internal policies prior to starting the course</p>
</div>

<h2 class="abs message-title teal-title">Get the message right!</h2>
<p class="abs message-text">Probably you can use 90 % of the course out of the box. But certain chapters will need to be aligned with your policies or risks. In a password security course you want to tell the user the correct tips in regard password length. In a course about malware you won't need to warn a user to not plugin an unknown USB device, if the USB port is anyway blocked</p>
<div class="abs" style="left:654px;top:3084px;width:457px;height:228px;background:linear-gradient(180deg,#f4f6f8 0%,#e7ecef 70%,#d9b98a 100%)" role="img" aria-label="Illustration of a presenter showing a password tip slide to an audience, with a large green tick"></div>

<div class="abs band-soft" style="top:3312px;height:319px;background:#f4f5f6"></div>

<svg class="abs" style="left:526px;top:3298px" width="136" height="108" viewBox="0 0 136 108" aria-hidden="true">
  <polygon points="0,18 18,0 118,0 136,18" fill="var(--grey-badge-dark)"/>
  <rect x="10" y="10" width="116" height="98" rx="10" fill="var(--grey-badge)"/>
  <text x="68" y="50" text-anchor="middle" font-family="Poppins,sans-serif" font-size="24" font-weight="300" fill="#fff">STEP</text>
  <text x="68" y="88" text-anchor="middle" font-family="Poppins,sans-serif" font-size="32" font-weight="700" fill="#fff">№4</text>
</svg>

<div class="abs" style="left:80px;top:3408px;width:228px;height:242px;border-radius:40%;background:linear-gradient(180deg,#ffc83a,#f09a1c)" role="img" aria-label="Mascot character sitting"></div>
<div class="abs" style="left:349px;top:3422px;width:167px;height:130px;border-radius:8px;background:linear-gradient(180deg,#1d5c9a,#0d3766)" role="img" aria-label="Blue folder illustration labelled for SCORM export"></div>

<h2 class="abs export-title">Export (Scorm)</h2>
<p class="abs export-text">Lorem Ipsum is simply dummy text of the printing and typesetting industry. Lorem Ipsum has been the industry's standard dummy text ever since the 1500s, when ...</p>

<footer class="abs footer"></footer>
<h6 class="abs f-head" style="left:88px;top:3746px">CONTACTS</h6>
<p class="abs f-lines" style="left:88px;top:3797px">Address: Europe<br>Brovantide Security AG<br>Lindenweg 12 | 8004 Zürich | Switzerland</p>
<p class="abs f-lines" style="left:88px;top:3899px">Address: North America<br>Brovantide Security USA<br>2210 Harbor Park Dr</p>

<h6 class="abs f-head" style="left:465px;top:3746px">SEARCH</h6>
<div class="abs search"><span>Search</span><i>
  <svg width="18" height="18" viewBox="0 0 18 18" aria-hidden="true"><circle cx="7.5" cy="7.5" r="5.5" fill="none" stroke="#8a9aa0" stroke-width="2"/><line x1="11.5" y1="11.5" x2="16" y2="16" stroke="#8a9aa0" stroke-width="2"/></svg>
</i></div>
<h6 class="abs f-head" style="left:465px;top:3883px">CONNECT</h6>
<div class="abs social"><span class="dot"></span>Friendbook</div>

<h6 class="abs f-head" style="left:735px;top:3746px">INFORMATION</h6>
<p class="abs f-lines" style="left:735px;top:3797px;line-height:33.3px">Home<br>Solution<br>Pricing<br>Resources<br>About us</p>

<h6 class="abs f-head" style="left:995px;top:3746px">LANGUAGE</h6>
<div class="abs lang">English
  <svg width="10" height="6" viewBox="0 0 10 6" aria-hidden="true"><polygon points="0,0 10,0 5,6" fill="#fff"/></svg>
</div>

<div class="abs f-rule"></div>
<p class="abs copyright center">Copyright 2020 | All Rights Reserved</p>
<div class="abs to-top">
  <svg width="12" height="8" viewBox="0 0 12 8" aria-hidden="true"><polyline points="1,7 6,2 11,7" fill="none" stroke="#fff" stroke-width="2"/></svg>
</div>

</body>
</html>
```